Presentation Folder for Brisk Estates

We are a new property management / real estate company in Denver Colorado and are in need of new stationary design. Attached are our business card and logo deigns. We are looking for our stationary design. We need a presentation folder design that is Professional, exciting, and approachable. We do not have a preference on folder layout (pockets, style of folding) but will most likely be using a standard two pocket folder design (roughly 9x12) but feel free to experiment with and folder style as long as we can find a place to print them. We would also like to have a matching letterhead/page design
Below is standard size of folder from lumo press
Full Bleed Size
20.87" x 16.68"
53 x 42.4 cm
6260 x 5004 pixels
Document Trim Size
20.75" x 16.56"
52.7 x 42.1 cm
6225 x 4969 pixels
Target Market(s)
We are attempting to target the top end of the real estate market in Denver Colorado. Are target market is investors in real estate.
Industry/Entity Type
Property Management
Font styles to use
Other font styles liked:
- Would like to keep font same to logo
Look and feel
Each slider illustrates characteristics of the customer's brand and the style your logo design should communicate.

```html
<!DOCTYPE html>
<html lang="en">
<head>
<meta charset="utf-8">
<title>Brisk Estates — Presentation Folder</title>
<link href="https://fonts.googleapis.com/css2?family=Oswald:wght@500&family=Open+Sans:wght@400;600&display=swap" rel="stylesheet">
<style>
  :root{
    --bg:#e9e9eb;
    --paper:#f7f7f8;
    --paper-shade:#ececee;
    --brand-blue:#4aa3c4;
    --brand-blue-soft:#7fc0d8;
    --brand-grey:#4a4a4c;
    --ink-soft:#8a8a8e;
    --edge:#d6d6da;
  }
  *{box-sizing:border-box;margin:0;padding:0}
  html,body{width:1200px;height:900px;overflow:hidden}
  body{background:var(--bg);font-family:"Open Sans",sans-serif;position:relative}

  .spread{position:absolute;top:230px;display:flex;box-shadow:0 18px 30px rgba(0,0,0,.12)}
  .spread--outer{left:45px}
  .spread--inner{left:615px}
  .panel{position:relative;width:270px;height:400px;background:var(--paper);overflow:hidden}
  .panel + .panel{border-left:1px solid var(--edge)}
  .panel--inside{background:var(--paper-shade)}

  .brand{display:flex;align-items:center;gap:7px}
  .brand__dot{width:22px;height:22px;border-radius:50%;background:var(--brand-blue);flex:none}
  .brand__name{font-family:"Oswald",sans-serif;font-weight:500;color:var(--brand-grey);text-transform:uppercase;letter-spacing:.5px;line-height:1;white-space:nowrap}
  .brand__tagline{font-size:7.5px;color:var(--brand-grey);margin-top:2px;letter-spacing:.2px;white-space:nowrap}

  /* back cover */
  .back__brand{position:absolute;top:110px;left:0;right:0;display:flex;justify-content:center}
  .back__brand .brand__name{font-size:11px}
  .back__brand .brand__dot{width:12px;height:12px}
  .back__arc{position:absolute;left:0;bottom:0}
  .back__contact{position:absolute;left:16px;bottom:16px;font-size:6px;line-height:1.5;color:var(--ink-soft);font-style:normal}

  /* front cover */
  .front__feature{position:absolute;left:0;top:0;width:270px;height:250px;
    background:linear-gradient(160deg,var(--brand-blue-soft) 0%,var(--brand-blue) 70%);}
  .front__brand{position:absolute;left:26px;bottom:70px}
  .front__brand .brand__name{font-size:22px}

  /* pockets */
  .pocket{position:absolute;left:0;right:0;bottom:0;height:118px;background:var(--paper);border-top:1px solid var(--edge);box-shadow:0 -2px 6px rgba(0,0,0,.05)}
  .pocket__brand{position:absolute;left:48px;top:42px}
  .pocket__brand .brand__name{font-size:15px}
  .pocket__brand .brand__dot{width:16px;height:16px}
  .pocket__brand .brand__tagline{font-size:5.5px}
  .pocket__arc{position:absolute;left:0;top:0}

  .card-slot{position:absolute;left:48px;top:-38px;width:160px;height:92px;background:#fff;box-shadow:0 2px 5px rgba(0,0,0,.18);padding:10px 10px 8px}
  .card__head{display:flex;justify-content:flex-end}
  .card__head .brand__name{font-size:9px}
  .card__head .brand__dot{width:10px;height:10px}
  .card__body{display:flex;justify-content:space-between;margin-top:14px;font-size:5px;line-height:1.55;color:var(--ink-soft)}
  .card__person strong{display:block;color:var(--brand-blue);font-weight:600}
</style>
</head>
<body>

  <section class="spread spread--outer" aria-label="Folder outside">
    <div class="panel panel--back">
      <div class="back__brand">
        <div class="brand">
          <span class="brand__dot"></span>
          <span class="brand__name">Brisk Estates</span>
        </div>
      </div>
      <svg class="back__arc" width="270" height="200" viewBox="0 0 270 200" aria-hidden="true">
        <path d="M0 120 Q120 60 270 92" fill="none" stroke="var(--brand-grey)" stroke-width="22"/>
      </svg>
      <address class="back__contact">
        1450 Market St<br>Denver, CO 80202<br>303 555 0147<br>briskestates.com
      </address>
    </div>
    <div class="panel panel--front">
      <div class="front__feature" role="img" aria-label="Large blue brand symbol decoration across the upper cover"></div>
      <div class="front__brand">
        <div class="brand">
          <span class="brand__dot"></span>
          <div>
            <div class="brand__name">Brisk Estates</div>
            <div class="brand__tagline">Property Management and Real Estate</div>
          </div>
        </div>
      </div>
    </div>
  </section>

  <section class="spread spread--inner" aria-label="Folder inside">
    <div class="panel panel--inside">
      <div class="pocket">
        <div class="pocket__brand">
          <div class="brand">
            <span class="brand__dot"></span>
            <div>
              <div class="brand__name">Brisk Estates</div>
              <div class="brand__tagline">Property Management and Real Estate</div>
            </div>
          </div>
        </div>
      </div>
    </div>
    <div class="panel panel--inside">
      <div class="pocket">
        <svg class="pocket__arc" width="270" height="118" viewBox="0 0 270 118" aria-hidden="true">
          <path d="M30 0 Q62 60 40 118" fill="none" stroke="var(--brand-grey)" stroke-width="14"/>
        </svg>
        <div class="card-slot">
          <div class="card__head">
            <div class="brand">
              <span class="brand__dot"></span>
              <span class="brand__name">Brisk Estates</span>
            </div>
          </div>
          <div class="card__body">
            <div class="card__person"><strong>Jordan Reed</strong>Managing Broker</div>
            <div>303 555 0148<br>303 555 0149<br>jordan@briskestates.com<br>briskestates.com</div>
          </div>
        </div>
      </div>
    </div>
  </section>

</body>
</html>
```